Corvallin Property Solutions need a business card design

Hello guys. We would need a business card design asap please.
We are a start up property investment business based in London UK specialised in buying, selling, managing and letting properties and helping distressed property owners.
The name of our Business is Corvallin, the logo symbolises the four fundamental elements of the world (earth, air, fire and water) and so it stands for strength, stability, longevity.
We would like the business card to communicate professionalism and reliability. Many many thanks indeed for your work.

Details:

1.) Marisol Dunkley
Property Investor
Mobile: +44(0)7700362517
Email: marisol.corvallin@quilbrook.example

2.) Tomas Brindle
Property Investor
Mobile: +44(0)7700845926
Email: tomas.corvallin@quilbrook.example

Industry/Entity Type

Investment

```html
<!DOCTYPE html>
<html lang="en">
<head>
<meta charset="utf-8">
<title>Corvallin Property Solutions — Business Card</title>
<link rel="stylesheet" href="https://fonts.googleapis.com/css2?family=Josefin+Sans:wght@700&family=Open+Sans:wght@400;600&display=swap">
<style>
  :root {
    --page-bg: #e9e7e4;
    --card-bg: #ffffff;
    --card-shadow: rgba(0, 0, 0, 0.14);
    --brand-grey: #8a8a8a;
    --brand-grey-light: #a3a3a3;
    --name-red: #c4162a;
    --title-blue: #2a5db0;
    --ink: #3a3a3a;
    --icon-blue: #3f6fb8;
    --mark-fill: #c4162a;
  }
  * { box-sizing: border-box; margin: 0; padding: 0; }
  html, body {
    width: 1200px;
    height: 720px;
    overflow: hidden;
    background: var(--page-bg);
  }
  .canvas {
    width: 1200px;
    height: 720px;
    display: flex;
    align-items: center;
    justify-content: center;
    gap: 40px;
  }
  .card {
    width: 540px;
    height: 310px;
    background: var(--card-bg);
    box-shadow: 0 6px 20px var(--card-shadow);
    position: relative;
  }
  .brand-name {
    font-family: "Josefin Sans", sans-serif;
    font-weight: 700;
    color: var(--brand-grey);
    letter-spacing: 0.06em;
    text-transform: uppercase;
    line-height: 1;
  }
  .brand-tagline {
    font-family: "Open Sans", sans-serif;
    font-weight: 600;
    color: var(--brand-grey-light);
    letter-spacing: 0.1em;
    text-transform: uppercase;
    line-height: 1;
  }
  .brand-square {
    background: var(--mark-fill);
    display: block;
  }

  /* Front: contact side */
  .card--front .brand-square {
    position: absolute;
    left: 70px;
    top: 95px;
    width: 120px;
    height: 120px;
  }
  .card--front .details {
    position: absolute;
    left: 255px;
    top: 52px;
  }
  .card--front .brand-name { font-size: 27px; }
  .card--front .brand-tagline { font-size: 10px; margin-top: 6px; padding-left: 2px; }
  .person { margin-top: 28px; font-family: "Open Sans", sans-serif; }
  .person-name { color: var(--name-red); font-weight: 600; font-size: 17px; line-height: 1.1; }
  .person-title { color: var(--title-blue); font-size: 12.5px; margin-top: 2px; }
  .contact { list-style: none; margin-top: 22px; font-family: "Open Sans", sans-serif; font-size: 12.5px; color: var(--ink); }
  .contact li { display: flex; align-items: center; gap: 10px; margin-bottom: 14px; }
  .contact svg { width: 13px; height: 13px; flex: none; fill: var(--icon-blue); }

  /* Back: brand side */
  .card--back {
    display: flex;
    flex-direction: column;
    align-items: center;
    justify-content: center;
  }
  .card--back .brand-square { width: 86px; height: 86px; margin-bottom: 34px; }
  .card--back .brand-name { font-size: 30px; }
  .card--back .brand-tagline { font-size: 11px; margin-top: 8px; }
</style>
</head>
<body>
<main class="canvas">
  <section class="card card--front" aria-label="Business card front">
    <span class="brand-square" aria-hidden="true"></span>
    <div class="details">
      <h1 class="brand-name">Corvallin</h1>
      <p class="brand-tagline">Property Solutions</p>
      <div class="person">
        <p class="person-name">Tomas Brindle</p>
        <p class="person-title">Property Investor</p>
      </div>
      <ul class="contact">
        <li>
          <svg viewBox="0 0 16 16" aria-hidden="true"><path d="M4 1h8a1 1 0 0 1 1 1v12a1 1 0 0 1-1 1H4a1 1 0 0 1-1-1V2a1 1 0 0 1 1-1zm1 2v8h6V3H5zm3 9.2a.9.9 0 1 0 0 1.8.9.9 0 0 0 0-1.8z"/></svg>
          +44(0)7700845926
        </li>
        <li>
          <svg viewBox="0 0 16 16" aria-hidden="true"><path d="M1 3h14v10H1V3zm1.6 1.2L8 8.4l5.4-4.2H2.6zM2.2 5.4v6.4h11.6V5.4L8 9.9 2.2 5.4z"/></svg>
          tomas.corvallin@quilbrook.example
        </li>
      </ul>
    </div>
  </section>

  <section class="card card--back" aria-label="Business card back">
    <span class="brand-square" aria-hidden="true"></span>
    <h2 class="brand-name">Corvallin</h2>
    <p class="brand-tagline">Property Solutions</p>
  </section>
</main>
</body>
</html>
```